Flyer for the Radiant Harvest Worship Day 2020

I am looking to create a flyer for a one day prayer retreat our church is organizing.
This flyer will be posted on social media, websites and will also be printed so it can be mailed to people.
I am looking for something professional, with good use of our logo and band colors (logo colors).
I am counting on the designer's skill, creativity, art and knowledge of media communication to produce a flyer that will effectively and quickly convey the message we are trying to spread.
CONTENT OF THE FLYER:
Event title: Radiant Harvest Worship Day
Date: Tuesday July 2nd, 2020
Time: 11:00AM - 7:00PM
Belmora Hotel, 4876 Willowmere Street, Portland, Maine 04987 (Room: Evergrove)
Event Key words to highlight what the event is about: Prayer, Sharing the Word, Panel discussion, prophecy, Impartation.
Key phrases:
A one day prayer retreat.
Jesus Chris is Lord
Contact info:
www.toluvek.org
Phone: 207 555 0183
Email: contact@brightmeadowfold.org

```html
<!DOCTYPE html>
<html lang="en">
<head>
<meta charset="utf-8">
<title>Radiant Harvest Worship Day 2020</title>
<link rel="stylesheet" href="https://fonts.googleapis.com/css2?family=Anton&family=Crimson+Pro:wght@400;600&family=Montserrat:wght@300;400&display=swap">
<style>
  :root {
    --navy-top: #023a60;
    --navy-mid: #022f4e;
    --night: #010407;
    --orange: #f7941d;
    --steel: #5f93ab;
    --sky: #86b8d2;
    --frame: #3d8fb5;
    --white: #ffffff;
  }
  * { margin: 0; padding: 0; box-sizing: border-box; }
  html, body { width: 1200px; height: 1000px; overflow: hidden; background: var(--white); }
  .flyer {
    position: absolute; left: 267px; top: 37px; width: 665px; height: 926px;
    background: linear-gradient(180deg, var(--navy-top) 0%, var(--navy-mid) 52%, #011a2b 75%, var(--night) 100%);
    overflow: hidden;
    font-family: "Crimson Pro", serif;
  }
  .abs { position: absolute; }
  .confession {
    left: 0; width: 665px; top: 24px; text-align: center;
    font-size: 19px; letter-spacing: 15px; padding-left: 15px; color: var(--steel);
  }
  .org-name {
    left: 0; width: 665px; top: 98px; text-align: center;
    font-size: 46px; font-weight: 400; color: var(--white); letter-spacing: 1px;
  }
  .org-name .dot {
    display: inline-block; width: 12px; height: 12px; border-radius: 50%;
    background: var(--orange); margin-right: 12px; vertical-align: middle;
  }
  .event-kicker {
    left: 0; width: 665px; top: 215px; text-align: center;
    font-family: "Montserrat", sans-serif; font-weight: 400; font-size: 26px;
    letter-spacing: 19px; padding-left: 19px; color: var(--white);
  }
  .event-title { left: 54px; top: 250px; width: 553px; height: 100px; }
  .event-title text { font-family: "Anton", sans-serif; fill: var(--orange); }
  .event-tagline {
    left: 0; width: 665px; top: 352px; text-align: center;
    font-size: 15px; letter-spacing: 12px; padding-left: 12px; color: var(--steel);
  }
  .date { right: 333px; top: 403px; text-align: right; color: var(--orange); }
  .date .weekday { font-size: 14px; letter-spacing: 2px; line-height: 16px; }
  .date .month { font-size: 32px; letter-spacing: 4px; line-height: 34px; margin-right: -3px; }
  .date .day {
    font-family: "Anton", sans-serif; font-size: 78px; line-height: 76px;
    color: var(--white); letter-spacing: 6px; margin-right: -6px;
  }
  .date .year {
    font-family: "Montserrat", sans-serif; font-weight: 300; font-size: 17px;
    letter-spacing: 10px; color: var(--white); margin-right: -10px; line-height: 26px;
  }
  .tag-box {
    border: 1.5px solid var(--frame); color: var(--white);
  }
  .tag-box::after {
    content: ""; position: absolute; right: -1.5px; bottom: -20px; width: 12px; height: 20px;
    background: var(--frame); clip-path: polygon(0 0, 100% 0, 0 100%);
  }
  .time-box { left: 357px; top: 417px; width: 212px; height: 38px; padding: 4px 0 0 7px; white-space: nowrap; }
  .time-box .clock { font-family: "Anton", sans-serif; font-size: 25px; letter-spacing: 2px; }
  .time-box sup { font-size: 7px; letter-spacing: 1px; vertical-align: 14px; margin: 0 3px 0 2px; }
  .time-box .to { font-size: 13px; letter-spacing: 1px; margin-right: 6px; }
  .program { left: 357px; top: 455px; list-style: none; color: var(--sky); }
  .program li { font-size: 16px; letter-spacing: 1.5px; line-height: 24px; }
  .venue-box { left: 357px; top: 615px; width: 178px; height: 38px; padding: 5px 0 0 7px; }
  .venue-box h2 { font-family: "Anton", sans-serif; font-weight: 400; font-size: 22px; letter-spacing: 4px; }
  .address { left: 357px; top: 660px; font-style: normal; color: var(--sky); }
  .address span { display: block; font-size: 12px; letter-spacing: 5px; line-height: 23px; }
  .call { left: 357px; top: 764px; color: var(--orange); }
  .call .label { font-family: "Anton", sans-serif; font-size: 15px; letter-spacing: 15px; line-height: 20px; }
  .call .number { font-family: "Montserrat", sans-serif; font-size: 23px; letter-spacing: 4px; line-height: 30px; }
  .contact { left: 0; width: 665px; text-align: center; color: var(--sky); font-size: 14px; }
  .contact.site { top: 871px; left: 100px; width: 600px; letter-spacing: 7px; }
  .contact.mail { top: 892px; left: 100px; width: 600px; letter-spacing: 4px; }
  .torch-art {
    left: 47px; top: 428px; width: 172px; height: 498px;
    background:
      radial-gradient(ellipse 48% 30% at 50% 32%, rgba(61,143,181,0.28), rgba(61,143,181,0) 100%),
      linear-gradient(180deg, rgba(61,143,181,0) 55%, rgba(61,143,181,0.16) 62%, rgba(61,143,181,0.10) 100%);
  }
</style>
</head>
<body>
  <main class="flyer">
    <p class="abs confession">JESUS CHRIS IS LORD</p>
    <h1 class="abs org-name"><span class="dot"></span>TOLUVEK</h1>

    <p class="abs event-kicker">RADIANT HARVEST</p>
    <svg class="abs event-title" viewBox="0 0 553 100" aria-label="Worship Day">
      <text x="0" y="96" font-size="124" textLength="553" lengthAdjust="spacingAndGlyphs">WORSHIP DAY</text>
    </svg>
    <p class="abs event-tagline">A ONE DAY PRAYER RETREAT</p>

    <div class="abs torch-art" role="img" aria-label="Outline drawing of a flaming torch in soft blue"></div>

    <div class="abs date">
      <div class="weekday">TUS</div>
      <div class="month">JULY</div>
      <div class="day">02</div>
      <div class="year">2020</div>
    </div>

    <div class="abs tag-box time-box">
      <span class="clock">11:00</span><sup>AM</sup><span class="to">TO</span><span class="clock">7:00</span><sup>PM</sup>
    </div>
    <ul class="abs program">
      <li>PRAYER</li>
      <li>SHARING THE WORD</li>
      <li>PANEL DISCUSSION</li>
      <li>PROPHECY</li>
      <li>IMPARTATION</li>
    </ul>

    <div class="abs tag-box venue-box"><h2>VENUE</h2></div>
    <address class="abs address">
      <span>BELMORA HOTEL</span>
      <span>4876 WILLOWMERE STREET</span>
      <span>PORTLAND, MAINE 04987</span>
      <span>(ROOM: EVERGROVE)</span>
    </address>

    <div class="abs call">
      <div class="label">CALL US</div>
      <div class="number">207 555 0183</div>
    </div>

    <p class="abs contact site">WWW.TOLUVEK.ORG</p>
    <p class="abs contact mail">EMAIL: CONTACT@BRIGHTMEADOWFOLD.ORG</p>
  </main>
</body>
</html>
```